Book cover for a book about time management for women

We need a book cover for a book about time management for women written by a woman. Even though the book has a provocative title "Calendar rebellion" based on the seminars the author holds for women seeking the change in their life, it has nothing to do with the words themselves. The subtitle is "Steer each day by choice. An opening guide on hour mastery among ladies"

Preferred fonts (not necessarily):
Plus Jakarta Sans
Tiempos Headline

Preferred colours (not necessarily):
- orange
- pastel "highlighters"

We look for a simple/clean design that catches the attention of the women without too many graphic elements.

Target Market(s)

Women that want to change and organise their life

Industry/Entity Type

productivity, marketing, work-life balance

Font styles to use
Other font styles liked:
• Plus Jakarta Sans, Tiempos Headline

Colors
F0912C
F2A743
F7CA91
FBE8D2
FDF5EE
A7469A
B969AE
D3A5CF
EDDBEB
F8F0F9

Requirements
Must have
• Famine feeling as the target audience are women with drive to better life
Should not have
• No explicit images or sexually motivated themes

```html
<!DOCTYPE html>
<html lang="en">
<head>
<meta charset="utf-8">
<title>Calendar Rebellion – Book Cover</title>
<link href="https://fonts.googleapis.com/css2?family=Antonio:wght@600;700&family=Lato:wght@400;700&display=swap" rel="stylesheet">
<style>
  :root {
    --page-bg: #ffffff;
    --cover-purple: #a64598;
    --disc-orange: #f8ac1a;
    --hill-orange: #f0a945;
    --title-white: #ffffff;
    --arc-blue: #2e6fa8;
  }
  html, body {
    margin: 0;
    padding: 0;
    width: 1200px;
    height: 1200px;
    overflow: hidden;
    background: var(--page-bg);
  }
  .canvas {
    position: relative;
    width: 1200px;
    height: 1200px;
  }
  .book-cover {
    position: absolute;
    left: 243px;
    top: 49px;
    width: 714px;
    height: 1102px;
  }
  .title-line-small,
  .title-line-large {
    font-family: 'Antonio', 'Oswald', sans-serif;
    fill: var(--title-white);
  }
  .title-line-small { font-weight: 600; }
  .title-line-large { font-weight: 700; }
  .tagline,
  .author-name {
    font-family: 'Lato', 'Helvetica Neue', Arial, sans-serif;
    fill: var(--title-white);
  }
  .tagline { font-weight: 700; }
  .arc-caption {
    font-family: 'Lato', 'Helvetica Neue', Arial, sans-serif;
    font-weight: 700;
    fill: var(--arc-blue);
    letter-spacing: 1px;
  }
</style>
</head>
<body>
<div class="canvas">
  <svg class="book-cover" viewBox="0 0 714 1102" xmlns="http://www.w3.org/2000/svg">
    <defs>
      <clipPath id="cover-clip"><rect width="714" height="1102"/></clipPath>
      <path id="caption-arc" d="M 146 840 A 215 215 0 0 1 576 840"/>
      <radialGradient id="clock-tone" cx="50%" cy="45%" r="55%">
        <stop offset="0%" stop-color="#e6ecf1"/>
        <stop offset="80%" stop-color="#d6e0e9"/>
        <stop offset="100%" stop-color="#3f78ad"/>
      </radialGradient>
    </defs>

    <g clip-path="url(#cover-clip)">
      <rect class="cover-background" width="714" height="1102" fill="var(--cover-purple)"/>

      <ellipse class="bottom-hill" cx="357" cy="1250" rx="520" ry="360" fill="var(--hill-orange)"/>

      <circle class="feature-disc" cx="358" cy="831" r="280" fill="var(--disc-orange)"/>

      <text class="title-line-small" x="78" y="192" font-size="100" textLength="558" lengthAdjust="spacingAndGlyphs">CALENDAR</text>
      <text class="title-line-large" x="80" y="486" font-size="330" textLength="556" lengthAdjust="spacingAndGlyphs">REBELLION</text>

      <text class="tagline" x="361" y="531" font-size="27" text-anchor="middle">STEER EACH DAY BY CHOICE</text>

      <text class="arc-caption" font-size="21">
        <textPath href="#caption-arc" startOffset="50%" text-anchor="middle">AN OPENING GUIDE ON HOUR MASTERY AMONG LADIES</textPath>
      </text>

      <circle class="clock-illustration" cx="361" cy="830" r="180" fill="url(#clock-tone)" role="img" aria-label="Illustration of a wall clock with a woman relaxing on its hands"/>

      <text class="author-name" x="357" y="1070" font-size="32" text-anchor="middle">AUTHOR NAME</text>
    </g>
  </svg>
</div>
</body>
</html>
```